The Copper Compass

we require a classy business card design for a business coaching company that uses our current logo and the wording:

Front of card:

LOGO
Glen Halvorsen
CEO
TEL: 1300 4 21953
FAX: 1300 6 21953
Mobile: 0419 627184
PO Box 217, Larkfield Rise, Brisbane, Qld 4163
e: glenh@coppercx.com.au
w: www.coppercx.com.au

Reverse side of the card:

Systematizing Businesses into Turnkey Operations
Strategic Business Plans
Sales & Marketing Programs
Sales Training & Business Coaching
Internet Marketing & Web Design

Here’s what our clients say:

“We grew from $396,000 to over $5million in 4 years and made QMT’s Rising Enterprise Honour Roll 3 years running!” – Simon Kearney, Meridel Works

small to medium sized business owners in Australia

Business

• standard business card size

```html
<!DOCTYPE html>
<html lang="en">
<head>
<meta charset="utf-8">
<title>The Copper Compass – Business Card</title>
<link rel="stylesheet" href="https://fonts.googleapis.com/css2?family=Questrial&display=swap">
<style>
  :root {
    --card-bg: #ffffff;
    --ink: #1a1a1a;
    --name-ink: #2a1c08;
    --glow: #f3b21f;
    --accent: #f2b428;
    --accent-deep: #ef8f22;
  }
  html, body {
    margin: 0;
    padding: 0;
    width: 1200px;
    height: 667px;
    overflow: hidden;
    background: var(--card-bg);
  }
  .card {
    position: relative;
    width: 1200px;
    height: 667px;
    background: var(--card-bg);
    font-family: "Questrial", "Century Gothic", sans-serif;
    color: var(--ink);
    overflow: hidden;
  }
  .corner-wedge {
    position: absolute;
    inset: 0;
    width: 1200px;
    height: 667px;
  }
  .brand {
    position: absolute;
    top: 118px;
    left: 0;
    width: 1200px;
    text-align: center;
    font-size: 70px;
    line-height: 1;
    color: var(--ink);
    margin: 0;
    font-weight: 400;
  }
  .holder {
    position: absolute;
    left: 34px;
    top: 338px;
    margin: 0;
    font-size: 41px;
    line-height: 52px;
    color: var(--name-ink);
    text-shadow: 0 0 6px var(--glow), 0 0 10px var(--glow);
    font-weight: 400;
  }
  .holder span { display: block; }
  .phones {
    position: absolute;
    left: 26px;
    top: 486px;
    margin: 0;
    padding: 0;
    list-style: none;
    font-size: 32px;
    line-height: 57px;
  }
  .address {
    position: absolute;
    right: 20px;
    top: 430px;
    margin: 0;
    padding: 0;
    list-style: none;
    text-align: right;
    font-size: 32px;
    line-height: 56px;
  }
</style>
</head>
<body>
<main class="card">
  <svg class="corner-wedge" viewBox="0 0 1200 667" aria-hidden="true">
    <polygon points="760,667 1200,330 1200,667" fill="var(--accent-deep)"/>
    <polygon points="800,667 1200,268 1200,667" fill="var(--accent)"/>
  </svg>

  <h1 class="brand">The Copper Compass</h1>

  <h2 class="holder">
    <span class="holder-name">Glen Halvorsen</span>
    <span class="holder-role">CEO</span>
  </h2>

  <ul class="phones">
    <li>TEL: 1300 4 21953</li>
    <li>FAX: 1300 6 21953</li>
    <li>Mobile: 0419 627184</li>
  </ul>

  <ul class="address">
    <li>PO Box 217, Larkfield Rise</li>
    <li>Brisbane, Qld 4163</li>
    <li>e: glenh@coppercx.com.au</li>
    <li>w: www.coppercx.com.au</li>
  </ul>
</main>
</body>
</html>
```